VitaNook Cookbook Cover

I need a design (front and back) for a cookbook cover. Our partners are looking for a few ideas to pick from.
You can see the style for one of the cookbooks we currently carry - uploaded with this brief.
This cookbook is a little different than most cookbooks out there. It is a cancer-fighting cookbook but we don't want it to be so cancer focused that people who don't have cancer will not buy. The book starts out with a section for Foods that Help, then goes to another section called Foods that Hurt. Then, we provide a Recipes section from the ingredients found in Foods that Help. Finally, the last section is called Beyond the Plate and deals with healthy lifestyle habits. You can see a rough draft of the content of the book at the link below. Please keep in mind that the current covers you see are not at all what we want. These were just put there to fill in the space.
Link for cookbook content: https://www.filecrate-example.net/s/4kq92mzx81pwtrd/The%20Bright%20Spoon%20-%20EDITED.pdf?dl=0
The title: The Bright Spoon
Subtitle: Fighting Cancer One Meal at a Time
Author: Mirel Tasvan
The company that puts the book out is VitaNook. It would be nice to have the logo somewhere small. Logo can be found here: https://www.filecrate-example.net/s/hzr37tqb05vnc2e/VitaNook%20Logo%20%26%20Guidelines.zip?dl=0
Like "Serve Them Sunnier Days" attached to this brief, we do NOT want something somber but more on the bright side. Just make it look nice and fresh. It would also be nice to somehow incorporate the concept of the cancer ribbon or a silhouette of it in a way that is not upfront but can still be acknowledge. No need for it to be pink and if that does not work, than it's better just to leave it out.
For the back cover, you can design it but simply leave room for us to fill in some text. No need for a spine design as it will be spiral bound.
The file must be designed and saved in PHOTOSHOP format.
According to the designer, the dimensions are:
207mm x 270mm + 5mm bleed
If you want to use the recipe pictures somehow in the cover, just snatch a picture from the content PDF and we can always replace it with the original larger file at a later time. Unfortunately, I don't have the pictures uploaded in filecrate.

```html
<!DOCTYPE html>
<html lang="en">
<head>
<meta charset="utf-8">
<title>The Bright Spoon — Cover</title>
<link rel="stylesheet" href="https://fonts.googleapis.com/css2?family=Marcellus&family=Josefin+Sans:ital,wght@0,300;1,200;1,300&display=swap">
<style>
  :root {
    --paper: #ffffff;
    --ink: #111111;
    --egg: #f2c23a;
    --crust: #c98a45;
    --cream: #f4efe6;
    --citrus: #f29a2a;
    --berry: #b8323f;
  }
  html, body {
    margin: 0;
    padding: 0;
    width: 960px;
    height: 1200px;
    overflow: hidden;
    background: var(--paper);
  }
  .cover {
    position: relative;
    width: 960px;
    height: 1200px;
    background: var(--paper);
    overflow: hidden;
  }
  .breakfast-photo {
    position: absolute;
    left: 35px;
    top: 214px;
    width: 925px;
    height: 986px;
    background:
      radial-gradient(ellipse 180px 160px at 430px 300px, rgba(184,50,63,0.35), transparent 70%),
      radial-gradient(ellipse 220px 200px at 760px 720px, rgba(201,138,69,0.75), transparent 70%),
      radial-gradient(ellipse 200px 180px at 120px 560px, rgba(242,194,58,0.85), transparent 70%),
      radial-gradient(ellipse 200px 150px at 830px 160px, rgba(242,154,42,0.8), transparent 70%),
      radial-gradient(ellipse 160px 140px at 170px 220px, rgba(160,120,80,0.55), transparent 70%),
      linear-gradient(90deg, #e7c9a0 0%, var(--cream) 40%, #f6f1ea 60%, #e8b872 100%);
  }
  .stripe {
    position: absolute;
    top: 214px;
    bottom: 0;
    background: var(--paper);
  }
  .title-the {
    position: absolute;
    left: 42px;
    top: 22px;
    font-family: "Josefin Sans", sans-serif;
    font-weight: 200;
    font-style: italic;
    font-size: 74px;
    line-height: 1;
    color: var(--ink);
  }
  .title-the span { display: inline-block; }
  .title-main {
    position: absolute;
    left: 56px;
    width: 864px;
    top: 62px;
    display: flex;
    justify-content: space-between;
    font-family: "Marcellus", serif;
    font-size: 122px;
    line-height: 1;
    color: var(--ink);
  }
  .title-tail {
    position: absolute;
    left: 652px;
    top: 146px;
    font-family: "Josefin Sans", sans-serif;
    font-weight: 200;
    font-style: italic;
    font-size: 90px;
    letter-spacing: 10px;
    line-height: 1;
    color: var(--ink);
  }
  .subtitle {
    position: absolute;
    left: 328px;
    top: 300px;
    transform-origin: 0 0;
    transform: rotate(90deg) translateY(-50%);
    white-space: nowrap;
    font-family: "Josefin Sans", sans-serif;
    font-weight: 300;
    font-size: 31px;
    letter-spacing: 9.4px;
    color: var(--ink);
  }
  .author {
    position: absolute;
    left: 630px;
    top: 1165px;
    transform-origin: 0 0;
    transform: rotate(-90deg) translateY(-50%);
    white-space: nowrap;
    font-family: "Josefin Sans", sans-serif;
    font-weight: 300;
    font-size: 22px;
    letter-spacing: 5px;
    color: var(--ink);
  }
</style>
</head>
<body>
  <main class="cover">
    <div class="breakfast-photo" role="img" aria-label="Bright breakfast table spread: scrambled eggs, bacon and sausages, a jar of oats, yogurt bowl with berries and granola, fruit salad, orange slices, juice, butter, jams and toast with strawberry jam"></div>

    <div class="stripe" style="left:51px;width:23px"></div>
    <div class="stripe" style="left:124px;width:22px"></div>
    <div class="stripe" style="left:160px;width:6px"></div>
    <div class="stripe" style="left:198px;width:44px"></div>
    <div class="stripe" style="left:294px;width:68px"></div>
    <div class="stripe" style="left:598px;width:68px"></div>
    <div class="stripe" style="left:718px;width:44px"></div>
    <div class="stripe" style="left:796px;width:4px;top:310px"></div>
    <div class="stripe" style="left:814px;width:22px"></div>
    <div class="stripe" style="left:886px;width:24px"></div>
    <div class="stripe" style="left:926px;width:8px"></div>

    <h1 class="book-title">
      <span class="title-the"><span>T</span><span style="transform:translateY(-8px)">h</span><span style="transform:translateY(10px)">e</span></span>
      <span class="title-main"><span>B</span><span>R</span><span>I</span><span>G</span><span>H</span><span>T</span></span>
      <span class="title-tail">Spoon</span>
    </h1>

    <p class="subtitle">fighting cancer one meal at a time</p>
    <p class="author">by Mirel Tasvan</p>
  </main>
</body>
</html>
```